Heritage Depot Business Cards

Require a business card design. <br/><br/>Needs to include logo (either round or long version) plus these details:<br/>Maya Corvell<br/>Heritage Depot<br/>maya@brightmarttrade.com.au<br/>02 6418 7395<br/>PO Box Glenfarrow NSW 2791<br/>www.heritagedepot.com.au<br/><br/>I need in an editable format so that I can create for multiple staff members. <br/><br/>

Target Market(s)

We are an online store selling renovation products to home owners are builders. Looking for a classic classy design.

Industry/Entity Type

Home And Garden

Contact Information for Business Card

Maya Corvell
Heritage Depot
maya@brightmarttrade.com.au
02 6418 7395
PO Box Glenfarrow NSW 2791
www.heritagedepot.com.au

Colors

Designer to choose colors to be used in the design.

Requirements
Must have
• Must include Logo.

```html
<!DOCTYPE html>
<html lang="en">
<head>
<meta charset="utf-8">
<title>Heritage Depot – Business Card</title>
<link href="https://fonts.googleapis.com/css2?family=Lato:wght@400;700&display=swap" rel="stylesheet">
<style>
  :root {
    --page-bg: #e6e1d9;
    --card-clear: #f3f0eb;
    --card-edge: #d6d0c6;
    --panel-dark: #0d0d0d;
    --panel-mid: #2a2a2a;
    --curve-shade: #8e8a84;
    --gold-light: #e2d3b4;
    --gold-text: #cfc0a2;
    --brand-ink: #1f1d1a;
  }
  * { margin: 0; padding: 0; box-sizing: border-box; }
  html, body {
    width: 1200px;
    height: 1047px;
    overflow: hidden;
    background: var(--page-bg);
    font-family: "Lato", sans-serif;
  }
  .business-card {
    position: absolute;
    left: 100px;
    top: 251px;
    width: 1000px;
    height: 544px;
    border-radius: 20px;
    background: var(--card-clear);
    border: 1px solid var(--card-edge);
    overflow: hidden;
  }
  .dark-panel {
    position: absolute;
    inset: 0;
    width: 1000px;
    height: 544px;
  }
  .contact-block {
    position: absolute;
    left: 31px;
    top: 0;
    color: var(--gold-text);
  }
  .person-name {
    position: absolute;
    top: 85px;
    white-space: nowrap;
    font-weight: 700;
    font-size: 41px;
    color: var(--gold-light);
  }
  .company-name {
    position: absolute;
    top: 148px;
    white-space: nowrap;
    font-size: 25px;
  }
  .postal-address {
    position: absolute;
    top: 263px;
    white-space: nowrap;
    font-size: 24px;
    line-height: 33px;
  }
  .contact-line {
    position: absolute;
    white-space: nowrap;
    font-size: 24px;
    display: flex;
    align-items: center;
  }
  .contact-line svg {
    width: 24px;
    height: 24px;
    margin-right: 22px;
    flex: none;
  }
  .line-phone { top: 356px; }
  .line-email { top: 392px; }
  .line-web { top: 429px; }
  .brand-mark {
    position: absolute;
    left: 618px;
    top: 133px;
    width: 278px;
    height: 278px;
    border: 2px solid var(--brand-ink);
    border-radius: 50%;
    display: flex;
    align-items: center;
    justify-content: center;
    text-align: center;
  }
  .brand-name {
    font-size: 38px;
    font-weight: 400;
    line-height: 44px;
    color: var(--brand-ink);
  }
</style>
</head>
<body>
  <div class="business-card">
    <svg class="dark-panel" viewBox="0 0 1000 544" aria-hidden="true">
      <defs>
        <linearGradient id="panelFill" x1="0" y1="0" x2="1" y2="0.3">
          <stop offset="0" stop-color="var(--panel-mid)"/>
          <stop offset="0.45" stop-color="var(--panel-dark)"/>
          <stop offset="1" stop-color="#1b1b1b"/>
        </linearGradient>
        <linearGradient id="shadeFill" x1="0" y1="0" x2="1" y2="0">
          <stop offset="0" stop-color="#5c5955"/>
          <stop offset="1" stop-color="var(--curve-shade)" stop-opacity="0.4"/>
        </linearGradient>
      </defs>
      <path d="M0,0 H571 Q426,272 542,544 H0 Z" fill="url(#shadeFill)"/>
      <path d="M0,0 H549 Q404,272 520,544 H0 Z" fill="url(#panelFill)"/>
    </svg>

    <div class="contact-block">
      <h1 class="person-name">Maya Corvell</h1>
      <p class="company-name">Heritage Depot</p>
      <p class="postal-address">PO Box Glenfarrow<br>NSW 2791</p>

      <p class="contact-line line-phone">
        <svg viewBox="0 0 24 24" fill="none" stroke="currentColor" stroke-width="1.8" stroke-linecap="round" stroke-linejoin="round">
          <path d="M5 3h3l2 5-2.5 1.5a11 11 0 0 0 7 7L16 14l5 2v3a2 2 0 0 1-2 2A16 16 0 0 1 3 5a2 2 0 0 1 2-2z"/>
        </svg>
        02 6418 7395
      </p>
      <p class="contact-line line-email">
        <svg viewBox="0 0 24 24" fill="none" stroke="currentColor" stroke-width="1.8" stroke-linejoin="round">
          <rect x="2" y="5" width="20" height="14"/>
          <path d="M2 5l10 8 10-8M2 19l7-7M22 19l-7-7"/>
        </svg>
        maya@brightmarttrade.com.au
      </p>
      <p class="contact-line line-web">
        <svg viewBox="0 0 24 24" fill="none" stroke="currentColor" stroke-width="1.6">
          <circle cx="12" cy="12" r="9.5"/>
          <ellipse cx="12" cy="12" rx="4" ry="9.5"/>
          <path d="M2.5 12h19M4 7h16M4 17h16"/>
        </svg>
        www.heritagedepot.com.au
      </p>
    </div>

    <div class="brand-mark">
      <p class="brand-name">Heritage<br>Depot</p>
    </div>
  </div>
</body>
</html>
```